Prestige Car Bodyshop Business Card

We are a car bodyshop based in the UK. Our customer base is mainly prestige high-value vehicles. I am looking for a classy and stylish business card design for my staff to give out to customers, with their direct email and phone number, as well as our main email and phone number with address details

I am also looking to have a general business card design with just our main company address and contact details, but also have a space to add a manufacturer approval logo (i.e Falcora, Vexa, Torvik etc... logo) in the corner somewhere.

I do not particularly want any outlines or pictures of cars on the card, I would just like a quality high-end look.

Please feel free to get in touch if you have any questions or queries?

Many Thanks

Gordon

Target Market(s)

Prestige vehicle owners

Industry/Entity Type

Automotive

Contact Information for Business Card

I am looking for a classy and stylish business card design for my staff to give out to customers, with their direct email and phone number, as well as our main email and phone number with address details

Font styles to use
Sans Serif

Colors

Designer to choose colors to be used in the design.

Requirements
Nice to have
• I do not particularly want any outlines or pictures of cars on the card, I would just like a quality high-end look.

```html
<!DOCTYPE html>
<html lang="en">
<head>
<meta charset="utf-8">
<title>Halden Accident Repair Centre – Business Card</title>
<link rel="stylesheet" href="https://fonts.googleapis.com/css2?family=Open+Sans:wght@300;400;600&display=swap">
<style>
  :root {
    --backdrop: #2b2b2c;
    --card-navy: #121c2c;
    --card-navy-deep: #0c1422;
    --edge-cyan: #1ec8d8;
    --accent-blue: #2a8fd6;
    --mark-blue: #2d5f9c;
    --text-light: #d9dde3;
    --text-soft: #b8c0cb;
    --rule: #c9ced6;
  }
  * { margin: 0; padding: 0; box-sizing: border-box; }
  html, body {
    width: 1200px; height: 720px; overflow: hidden;
    background: var(--backdrop);
    font-family: "Open Sans", Arial, sans-serif;
  }
  .canvas {
    width: 1200px; height: 720px;
    display: flex; align-items: center; justify-content: center;
  }
  .business-card {
    position: relative;
    width: 900px; height: 520px;
    background: radial-gradient(ellipse at 40% 30%, var(--card-navy), var(--card-navy-deep));
    border-bottom: 6px solid var(--edge-cyan);
    box-shadow: 0 24px 50px rgba(0,0,0,.55);
  }
  .brand {
    position: absolute; left: 70px; top: 150px;
    display: flex; align-items: center; gap: 26px;
  }
  .brand-mark {
    width: 130px; height: 130px; border-radius: 50%;
    background: var(--mark-blue);
  }
  .brand-name {
    font-weight: 300; font-size: 50px; letter-spacing: 3px;
    color: var(--text-light); line-height: 1;
    padding-bottom: 10px;
    border-bottom: 2px solid var(--rule);
  }
  .brand-tagline {
    margin-top: 8px;
    font-weight: 300; font-size: 15px; letter-spacing: 1.5px;
    color: var(--text-soft);
  }
  .staff {
    position: absolute; left: 590px; top: 110px;
  }
  .staff-name { font-size: 22px; font-weight: 400; color: var(--accent-blue); }
  .staff-title { margin-left: 18px; font-size: 14px; color: var(--text-light); }
  .contact-row {
    position: absolute; left: 70px; right: 50px; bottom: 70px;
    display: flex; align-items: center;
  }
  .contact-item {
    display: flex; align-items: center; gap: 10px;
    font-size: 20px; font-weight: 300; color: var(--text-light);
    white-space: nowrap;
  }
  .contact-item svg { flex: none; }
  .divider {
    width: 2px; height: 90px; margin: 0 36px;
    background: linear-gradient(to bottom, transparent, var(--accent-blue), transparent);
    transform: skewX(-18deg);
  }
</style>
</head>
<body>
<main class="canvas">
  <section class="business-card">
    <div class="brand">
      <div class="brand-mark"></div>
      <div class="brand-text">
        <div class="brand-name">HALDEN</div>
        <div class="brand-tagline">ACCIDENT REPAIR CENTRE</div>
      </div>
    </div>

    <div class="staff">
      <div class="staff-name">Gordon</div>
      <div class="staff-title">Title</div>
    </div>

    <div class="contact-row">
      <div class="contact-item phone">
        <svg width="18" height="18" viewBox="0 0 24 24" aria-hidden="true">
          <path fill="#2a8fd6" d="M6.6 10.8a15.1 15.1 0 0 0 6.6 6.6l2.2-2.2a1 1 0 0 1 1-.25 11.4 11.4 0 0 0 3.6.57 1 1 0 0 1 1 1V20a1 1 0 0 1-1 1A17 17 0 0 1 3 4a1 1 0 0 1 1-1h3.5a1 1 0 0 1 1 1c0 1.25.2 2.45.57 3.57a1 1 0 0 1-.25 1z"/>
        </svg>
        <span>0117 496 0382</span>
      </div>
      <div class="divider"></div>
      <div class="contact-item web">
        <svg width="20" height="20" viewBox="0 0 24 24" aria-hidden="true" fill="none" stroke="#2a8fd6" stroke-width="1.6">
          <circle cx="12" cy="12" r="9"/><ellipse cx="12" cy="12" rx="4" ry="9"/><path d="M3 12h18M5 7h14M5 17h14"/>
        </svg>
        <span>www.haldenrepair.co.uk</span>
      </div>
      <div class="divider"></div>
      <div class="contact-item email">
        <svg width="20" height="16" viewBox="0 0 24 18" aria-hidden="true" fill="none" stroke="#2a8fd6" stroke-width="1.8">
          <rect x="1" y="1" width="22" height="16"/><path d="M1 1l11 9 11-9"/>
        </svg>
        <span>info@haldenrepair.co.uk</span>
      </div>
    </div>
  </section>
</main>
</body>
</html>
```